Improve on a PowerPoint Design

I need the attached PPTX to have a professional design.

There needs to be logos for each of the quadrants - ideally the company logo or something similar

```html
<!DOCTYPE html>
<html lang="en">
<head>
<meta charset="utf-8">
<title>AI &amp; Business Transformation Framework</title>
<link href="https://fonts.googleapis.com/css2?family=Poppins:wght@400;500;700;800&display=swap" rel="stylesheet">
<style>
  :root {
    --navy: #134886;
    --navy-deep: #0d4a8f;
    --blue-mid: #2b65a5;
    --blue-soft: #3a6ea8;
    --heading: #1a4f96;
    --ink: #1b1f2a;
    --dash: #3a3f4a;
    --paper: #ffffff;
    --title-shadow: #0a1f3d;
  }
  html, body {
    margin: 0;
    padding: 0;
    overflow: hidden;
    background: var(--paper);
  }
  .canvas {
    position: relative;
    width: 1200px;
    height: 675px;
    overflow: hidden;
    background: var(--paper);
    font-family: "Poppins", sans-serif;
    color: var(--ink);
  }
  .shapes {
    position: absolute;
    inset: 0;
  }
  .title-pill {
    position: absolute;
    left: 204px;
    top: 29px;
    width: 793px;
    height: 74px;
    border-radius: 37px;
    background: var(--navy);
    display: flex;
    align-items: center;
    justify-content: center;
  }
  .title-pill h1 {
    margin: 0;
    color: var(--paper);
    font-weight: 800;
    font-size: 30px;
    letter-spacing: 0.2px;
    text-shadow: 2px 2px 0 var(--title-shadow);
  }
  .pillar-label {
    position: absolute;
    width: 258px;
    height: 42px;
    box-sizing: border-box;
    border: 1px dashed var(--dash);
    border-radius: 21px;
    display: flex;
    align-items: center;
    justify-content: center;
    margin: 0;
    color: var(--heading);
    font-weight: 500;
    font-size: 23px;
    line-height: 1;
  }
  .pillar-label.workshops { left: 54px; top: 200px; }
  .pillar-label.analytics { left: 54px; top: 406px; }
  .pillar-label.citizen { left: 865px; top: 200px; }
  .pillar-label.power { left: 865px; top: 406px; }
  .points {
    position: absolute;
    margin: 0;
    padding: 0;
    list-style: none;
    font-size: 14.5px;
    line-height: 1.25;
  }
  .points li {
    position: relative;
    padding-left: 19px;
    margin-bottom: 9px;
  }
  .points li::before {
    content: "";
    position: absolute;
    left: 0;
    top: 4px;
    width: 9px;
    height: 9px;
    border: 1.2px solid var(--ink);
    border-radius: 50%;
  }
  .points li::after {
    content: "";
    position: absolute;
    left: 3px;
    top: 7.5px;
    width: 3px;
    height: 3px;
    border-top: 1.2px solid var(--ink);
    border-right: 1.2px solid var(--ink);
    transform: rotate(45deg);
  }
  .points.workshops { left: 98px; top: 250px; }
  .points.workshops li { margin-bottom: 0; }
  .points.analytics { left: 98px; top: 457px; }
  .points.analytics li { margin-bottom: 9.5px; }
  .points.citizen { left: 876px; top: 250px; }
  .points.citizen li { padding-left: 22px; margin-bottom: 10px; }
  .points.power { left: 876px; top: 457px; }
  .points.power li { padding-left: 18px; margin-bottom: 9.5px; }
</style>
</head>
<body>
<main class="canvas">
  <svg class="shapes" width="1200" height="675" viewBox="0 0 1200 675" xmlns="http://www.w3.org/2000/svg">
    <defs>
      <radialGradient id="hero-tone" cx="0.45" cy="0.45" r="0.7">
        <stop offset="0" stop-color="#3b6fd6"/>
        <stop offset="0.55" stop-color="#2a3f9e"/>
        <stop offset="1" stop-color="#1c2566"/>
      </radialGradient>
      <marker id="arrow-tip" viewBox="0 0 10 10" refX="5" refY="5" markerWidth="4" markerHeight="4" orient="auto">
        <path d="M0,0 L10,5 L0,10 Z" fill="#ffffff"/>
      </marker>
    </defs>

    <!-- title connectors -->
    <g class="title-connectors" fill="none" stroke="var(--navy)" stroke-width="2.5">
      <path d="M155,41 C155,60 170,70 204,70"/>
      <path d="M997,70 C1040,70 1069,75 1069,100"/>
    </g>
    <circle cx="155" cy="41" r="3" fill="var(--navy)"/>
    <circle cx="1069" cy="100" r="3" fill="var(--navy)"/>

    <!-- dashed leaders -->
    <g class="leaders" fill="none" stroke="var(--dash)" stroke-width="0.8" stroke-dasharray="3 2">
      <path d="M312,220 L408,220 L422,242"/>
      <path d="M312,426 L395,426 L411,443"/>
      <path d="M865,219 L783,219 L766,238"/>
      <path d="M865,426 L799,426 L783,443"/>
    </g>

    <!-- cycle ring -->
    <g class="cycle-ring">
      <path d="M596,353 L390,353 A206,206 0 0 1 596,147 Z" fill="var(--navy-deep)"/>
      <path d="M596,353 L596,147 A206,206 0 0 1 802,353 Z" fill="var(--blue-soft)"/>
      <path d="M596,353 L802,353 A206,206 0 0 1 596,559 Z" fill="var(--navy-deep)"/>
      <path d="M596,353 L596,559 A206,206 0 0 1 390,353 Z" fill="var(--blue-mid)"/>
      <circle cx="596" cy="353" r="158" fill="#ffffff"/>
      <circle cx="596" cy="353" r="147" fill="url(#hero-tone)" role="img" aria-label="Illustration of artificial intelligence and a digital city with a glowing globe"/>
    </g>

    <!-- flow arrows -->
    <g class="flow-arrows" fill="none" stroke="#ffffff" stroke-width="2.5" stroke-linecap="round" marker-end="url(#arrow-tip)">
      <path d="M573,172 Q592,167 612,171"/>
      <path d="M780,320 Q784,340 780,358"/>
      <path d="M617,535 Q598,541 578,537"/>
      <path d="M413,372 Q409,352 413,333"/>
    </g>

    <!-- quadrant badges -->
    <g class="badge badge-ai">
      <circle cx="474" cy="261" r="41" fill="#ffffff"/>
      <circle cx="474" cy="261" r="37" fill="var(--navy)"/>
      <rect x="459" y="246" width="30" height="30" rx="2" fill="none" stroke="#ffffff" stroke-width="2"/>
      <rect x="463" y="250" width="22" height="22" fill="none" stroke="#ffffff" stroke-width="1.2"/>
      <text x="474" y="267" text-anchor="middle" fill="#ffffff" font-family="Poppins, sans-serif" font-weight="700" font-size="13">AI</text>
      <g stroke="#ffffff" stroke-width="1.5" stroke-dasharray="2 2">
        <path d="M461,243 H487"/><path d="M461,279 H487"/>
        <path d="M456,248 V274"/><path d="M492,248 V274"/>
      </g>
    </g>
    <g class="badge badge-growth">
      <circle cx="720" cy="259" r="41" fill="#ffffff"/>
      <circle cx="720" cy="259" r="37" fill="var(--navy)"/>
      <g fill="#ffffff">
        <rect x="698" y="266" width="7" height="12"/>
        <rect x="708" y="259" width="7" height="19"/>
        <rect x="718" y="252" width="7" height="26"/>
        <rect x="728" y="244" width="7" height="34"/>
        <path d="M726,244 L731.5,235 L737,244 Z"/>
        <rect x="696" y="278" width="45" height="2.5"/>
      </g>
    </g>
    <g class="badge badge-analytics">
      <circle cx="471" cy="443" r="41" fill="#ffffff"/>
      <circle cx="471" cy="443" r="37" fill="var(--blue-mid)"/>
      <g fill="none" stroke="#ffffff" stroke-width="1.5">
        <rect x="446" y="427" width="42" height="31"/>
        <path d="M450,433 H462 M450,438 H462 M450,443 H462"/>
        <path d="M465,443 L473,436 L480,439 L489,429"/>
        <circle cx="489" cy="424" r="3.5" fill="#ffffff"/>
        <rect x="450" y="449" width="3" height="6"/>
        <rect x="456" y="446" width="3" height="9"/>
        <rect x="462" y="448" width="3" height="7"/>
        <circle cx="482" cy="457" r="8" fill="var(--blue-mid)"/>
        <circle cx="482" cy="457" r="4"/>
      </g>
    </g>
    <g class="badge badge-process">
      <circle cx="720" cy="443" r="41" fill="#ffffff"/>
      <circle cx="720" cy="443" r="37" fill="var(--navy-deep)"/>
      <g fill="none" stroke="#ffffff" stroke-width="1.5">
        <circle cx="721" cy="424" r="4.5"/>
        <path d="M713,437 Q721,429 729,437"/>
        <path d="M710,438 V427 H704 M706,424 L703,427 L706,430"/>
        <path d="M732,427 H737 V438 M734,435 L737,438 L740,435"/>
        <rect x="699" y="447" width="11" height="15"/>
        <path d="M701,451 H708 M701,455 H708 M701,459 H708"/>
        <path d="M724,454 H715 M718,451 L715,454 L718,457"/>
        <circle cx="736" cy="454" r="6"/>
        <circle cx="736" cy="454" r="2.5"/>
        <circle cx="736" cy="454" r="8.5" stroke-dasharray="2.5 2.5" stroke-width="2.5"/>
      </g>
    </g>
  </svg>

  <header class="title-pill">
    <h1>AI &amp; BUSINESS TRANSFORMATION FRAMEWORK</h1>
  </header>

  <h2 class="pillar-label workshops">AI Workshops</h2>
  <ul class="points workshops">
    <li>Identify use cases of generative<br>AI with business leaders</li>
  </ul>

  <h2 class="pillar-label analytics">Analytiq</h2>
  <ul class="points analytics">
    <li>Data Analytics Engine</li>
    <li>Server and Staff PCs</li>
    <li>Initial focus on Audit</li>
  </ul>

  <h2 class="pillar-label citizen">Citizen Development</h2>
  <ul class="points citizen">
    <li>Launched Q1 2023</li>
    <li>BotLane RPA</li>
  </ul>

  <h2 class="pillar-label power">Cobalt Power Tools</h2>
  <ul class="points power">
    <li>Extension to Citize Developer</li>
    <li>Bootcamp planned for X</li>
  </ul>
</main>
</body>
</html>
```